Design a CD Cover For Baby Music and Lullabies To Appear on Tune Harbor Shop etc.

Please read this brief before you design. Otherwise you will be wasting your time.

I need a cd cover for music albums which will appear on streaming sites such as Tune Harbor Shop Wavelane, Pluvix etc. for the brand Cozy Cradle Tunes. The thumbnails are quite small so the text needs to be quite large.

I need a design if possible, in which I can simply alter the title of the album and the baby picture so that each album has a different cover but works with the branding.

You can check out the Cozy Cradle Tunes on the Tune Harbor shop.
https://play.wavelane.example/artist/7qk3RtLmWvNx82hYbPdaZe

I made those covers and I really don't like them at all! As you can tell I am not a graphic designer. Ha.

Please help me with a modern, eye catching and cute design that will work across the brand now and in the future. The CCT logo and the name Cozy Cradle Tunes is the only thing that needs to be used somewhere in the design.

Please use the title

Soft Hush Tones For Nap Time Part First

for this first album.
(White noise sounds are hair dryers, vacuum cleaners, fans, wind, rain, the sea, white noise, pink noise, brown noise etc. )

Here is an example of album covers which are coherent. A style like this without the over the top text would be good. But don't copy these!
https://play.wavelane.example/artist/9TfKxcMnEuGh31oAsQbiR5

Target Market(s)

Parents of babies.

Font styles to use
Serif
Sans Serif

Colors

Designer to choose colors to be used in the design.

Requirements
Must have
• Large font so it can been seen in the wavelane thumbnail. A photo of a baby. Please take a look at the wavelane and tune harbor stores. The Cozy Cradle Tunes logo.
• Album Title
• Soft Hush Tones For Nap Time Part First

```html
<!DOCTYPE html>
<html lang="en">
<head>
<meta charset="utf-8">
<title>Soft Hush Tones For Nap Time – Part First</title>
<link href="https://fonts.googleapis.com/css2?family=Oswald:wght@300;400&family=Montserrat:wght@700&display=swap" rel="stylesheet">
<style>
  :root {
    --backdrop-top: #e8d8cd;
    --backdrop-mid: #8d827d;
    --backdrop-bottom: #171717;
    --sheet-blue: #a8c3d4;
    --sheet-light: #c4d8e4;
    --cloud-cream: #f6ece4;
    --blush: #f2a391;
    --title-white: #ffffff;
    --title-navy: #0d2a7a;
    --badge-fill: #1f8fd6;
    --caption: #ffffff;
  }
  * { margin: 0; padding: 0; box-sizing: border-box; }
  html, body { width: 1200px; height: 1200px; overflow: hidden; }
  body {
    position: relative;
    background: linear-gradient(180deg, var(--backdrop-top) 0%, #c9b9b0 22%, var(--backdrop-mid) 50%, #3a3634 75%, var(--backdrop-bottom) 100%);
    font-family: "Oswald", sans-serif;
  }
  .album-cover {
    position: absolute;
    left: 181px;
    top: 131px;
    width: 847px;
    height: 847px;
    overflow: hidden;
  }
  .cover-photo {
    position: absolute;
    inset: 0;
    background:
      radial-gradient(ellipse 45% 30% at 52% 52%, rgba(240,236,232,0.55), transparent 70%),
      radial-gradient(ellipse 70% 30% at 40% 92%, rgba(242,163,145,0.85), transparent 70%),
      linear-gradient(180deg, var(--sheet-light) 0%, var(--sheet-blue) 55%, var(--cloud-cream) 82%, #f3d9cf 100%);
  }
  .album-title {
    position: absolute;
    top: 112px;
    left: 0;
    width: 100%;
    text-align: center;
    font-weight: 300;
    text-transform: uppercase;
    line-height: 1;
  }
  .album-title .title-line {
    display: block;
    font-size: 112px;
    letter-spacing: 3px;
  }
  .title-line--light { color: var(--title-white); }
  .title-line--accent { color: var(--title-navy); font-weight: 400; margin-top: 2px; }
  .album-part {
    position: absolute;
    top: 728px;
    left: 200px;
    font-size: 56px;
    font-weight: 300;
    letter-spacing: 22px;
    color: var(--title-navy);
    text-transform: uppercase;
  }
  .brand-mark {
    position: absolute;
    right: 38px;
    bottom: 40px;
    display: flex;
    flex-direction: column;
    align-items: center;
    gap: 6px;
  }
  .brand-mark .brand-dot {
    width: 80px;
    height: 80px;
    border-radius: 50%;
    background: var(--badge-fill);
  }
  .brand-mark .brand-name {
    font-size: 16px;
    font-weight: 400;
    color: var(--title-navy);
    letter-spacing: 1px;
    white-space: nowrap;
  }
  .cover-caption {
    position: absolute;
    top: 1008px;
    left: 0;
    width: 100%;
    text-align: center;
    font-family: "Montserrat", sans-serif;
    font-weight: 700;
    font-size: 45px;
    letter-spacing: 3px;
    line-height: 60px;
    color: var(--caption);
  }
</style>
</head>
<body>
  <main class="album-cover">
    <div class="cover-photo" role="img" aria-label="Photo of a sleeping baby lying on a light blue sheet, lower half fading into soft cream and pink clouds"></div>
    <h1 class="album-title">
      <span class="title-line title-line--light">Soft Hush Tones</span>
      <span class="title-line title-line--accent">For Nap Time</span>
    </h1>
    <p class="album-part">Part First</p>
    <div class="brand-mark">
      <span class="brand-dot"></span>
      <span class="brand-name">Cozy Cradle Tunes</span>
    </div>
  </main>
  <p class="cover-caption">Soft Hush Tones<br>for Nap Time</p>
</body>
</html>
```